Pelin Thai Massage Double Sided Flyer Luxury

I require a double sided flyer
we are a Thai Massage Spa
Would like gold, deep purple and bronze colours
Something eye catching and looks professional

```html
<!DOCTYPE html>
<html lang="en">
<head>
<meta charset="utf-8">
<title>Pelin Thai Massage – Double Sided Flyer</title>
<link rel="stylesheet" href="https://fonts.googleapis.com/css2?family=Montserrat:wght@400;500;600;700;800&family=Lobster&display=swap">
<style>
  :root{
    --bg:#e6e6e6;
    --paper:#ffffff;
    --purple:#860a8a;
    --purple-deep:#6e0a74;
    --purple-bright:#960c97;
    --lavender:#efe2f0;
    --lilac:#e6dbeb;
    --gold:#efb222;
    --ink:#161616;
    --sans:'Montserrat', Arial, sans-serif;
    --script:'Lobster', cursive;
  }
  *{box-sizing:border-box;margin:0;padding:0}
  html,body{width:1200px;height:538px;overflow:hidden;background:var(--bg)}
  .canvas{position:relative;width:1200px;height:538px;font-family:var(--sans);color:var(--ink)}
  .page{position:absolute;top:19px;width:354px;height:500px;background:var(--paper);overflow:hidden;box-shadow:0 1px 4px rgba(0,0,0,.08)}
  .page--front{left:234px}
  .page--back{left:612px}
  .block{position:absolute}

  /* front */
  .brand{position:absolute;left:12px;top:14px;width:88px;text-align:center}
  .brand__dot{display:block;width:24px;height:24px;border-radius:50%;background:var(--gold);margin:0 auto 10px}
  .brand__name{font-size:8.6px;font-weight:500;color:var(--gold);white-space:nowrap}
  .tile--lilac-top{left:291px;top:0;width:63px;height:42px;background:var(--lilac)}
  .tile--purple-large{left:223px;top:42px;width:131px;height:84px;background:linear-gradient(90deg,var(--purple-deep),var(--purple-bright))}
  .tile--lilac-small{left:175px;top:56px;width:45px;height:34px;background:var(--lilac)}
  .tile--purple-wide{left:110px;top:90px;width:110px;height:36px;background:linear-gradient(90deg,var(--purple-deep),var(--purple-bright))}
  .frame--lavender{left:86px;top:103px;width:24px;height:281px;background:var(--lavender)}
  .tile--lilac-corner{left:340px;top:396px;width:14px;height:24px;background:var(--lilac)}
  .photo--treatment{left:96px;top:130px;width:258px;height:254px;background:linear-gradient(135deg,#5a4a3c 0%,#c9a58c 45%,#e7c3aa 60%,#9cb03a 100%)}
  .voucher{position:absolute;left:220px;top:368px;width:134px;height:28px;background:var(--purple);color:#fff;font-family:var(--script);font-size:11.5px;display:flex;align-items:center;justify-content:center;letter-spacing:.2px}
  .headline--welcome{position:absolute;left:10px;bottom:12px;writing-mode:vertical-rl;transform:rotate(180deg);line-height:.95}
  .headline--welcome .line1{display:block;font-size:31px;font-weight:500;color:var(--ink)}
  .headline--welcome .line2{display:block;font-size:38px;font-weight:800;color:var(--purple);letter-spacing:.5px}
  .intro{position:absolute;left:96px;top:403px;width:212px;font-size:7px;line-height:10.7px;font-weight:500}
  .intro p+p{margin-top:10.7px}

  /* back */
  .photo--room{left:0;top:0;width:273px;height:190px;background:linear-gradient(160deg,#8a7868 0%,#d8c8b4 40%,#f1e6d6 60%,#7a5a40 100%)}
  .strip--top{left:273px;top:0;width:9px;height:176px;background:var(--lavender)}
  .headline--packages{position:absolute;right:9px;top:12px;writing-mode:vertical-rl;line-height:1}
  .headline--packages .line1{display:block;font-size:25px;font-weight:500;color:var(--ink);letter-spacing:-.6px}
  .headline--packages .line2{display:block;font-size:26px;font-weight:800;color:var(--purple);letter-spacing:-1.4px}
  .photo--bed{left:0;top:194px;width:141px;height:78px;background:linear-gradient(150deg,#3a2a20 0%,#e9e3dc 45%,#6a3a22 100%)}
  .strip--mid{left:141px;top:199px;width:10px;height:65px;background:var(--lilac)}
  .bar--purple{left:0;top:276px;width:141px;height:13px;background:linear-gradient(90deg,var(--purple-deep),var(--purple-bright))}
  .pitch{position:absolute;left:157px;top:209px;width:190px}
  .pitch__lead{font-family:var(--script);font-size:9.8px;color:var(--ink)}
  .pitch__name{font-size:10.4px;font-weight:700;line-height:13px;margin-top:1px}
  .pitch__text{font-size:10.4px;font-weight:500;line-height:13px}
  .pitch__list{list-style:none;margin-top:5px}
  .pitch__list li{display:flex;align-items:center;gap:5px;font-size:7.8px;font-weight:500;height:13px}
  .pitch__list svg{width:9px;height:9px;flex:none}
  .menu{position:absolute;left:0;top:308px;width:354px;height:134px;background:var(--lavender);padding:12px 10px 0}
  .treatment__title{font-size:12.6px;font-weight:700;letter-spacing:.2px}
  .treatment+.treatment{margin-top:14px}
  .treatment__rows{display:flex;margin-top:7px}
  .option{display:flex;gap:10px;width:168px}
  .option__price{font-size:11.5px;font-weight:700;color:var(--purple);line-height:11px}
  .option__time{display:block;font-size:7px;font-weight:700;color:var(--ink);line-height:10px}
  .option__desc{font-size:7.6px;font-weight:500;line-height:11px;padding-top:1px}
  .opening{position:absolute;right:12px;top:450px;font-size:10.5px;font-weight:700;letter-spacing:.3px}
  .contact{position:absolute;left:0;bottom:0;width:354px;height:31px;background:linear-gradient(90deg,var(--purple-deep),var(--purple-bright));display:flex;align-items:center;justify-content:space-between;padding:0 10px 0 8px;color:#fff;font-size:6.9px;font-weight:600}
  .contact__item{display:flex;align-items:center;gap:3px;white-space:nowrap}
  .contact__item svg{width:7px;height:7px;flex:none}
</style>
</head>
<body>
<div class="canvas">

  <section class="page page--front" aria-label="Flyer front">
    <div class="brand">
      <span class="brand__dot"></span>
      <span class="brand__name">Pelin Thai Massage</span>
    </div>
    <div class="block tile--lilac-top"></div>
    <div class="block tile--purple-large"></div>
    <div class="block tile--lilac-small"></div>
    <div class="block tile--purple-wide"></div>
    <div class="block frame--lavender"></div>
    <div class="block photo--treatment" role="img" aria-label="Photo of a woman relaxing on a green towel while receiving a back massage"></div>
    <div class="voucher">Gift Vouchers Available</div>
    <div class="block tile--lilac-corner"></div>
    <h1 class="headline--welcome"><span class="line1">Welcome to</span><span class="line2">LUXURY</span></h1>
    <div class="intro">
      <p>Set in the heart of Ashgrove,<br>Pelin Thai Massage will allow you to immerse yourself in a place where your wellbeing &amp; rejuvenation is at the centre of what we do.</p>
      <p>Using Thai traditions, our highly trained therapists offer revitalising body treatments with their deep tissue massage techniques. In their hands, you will see &amp; feel</p>
    </div>
  </section>

  <section class="page page--back" aria-label="Flyer back">
    <div class="block photo--room" role="img" aria-label="Photo of a warm, softly lit spa treatment room with a massage table"></div>
    <div class="block strip--top"></div>
    <h2 class="headline--packages"><span class="line1">Massage</span><span class="line2">PACKAGES</span></h2>
    <div class="block photo--bed" role="img" aria-label="Photo of a massage bed with white towels on a wooden floor"></div>
    <div class="block strip--mid"></div>
    <div class="block bar--purple"></div>
    <div class="pitch">
      <p class="pitch__lead">Discover all the ways</p>
      <p class="pitch__name">PELIN THAI MASSAGE</p>
      <p class="pitch__text">can breathe new life into<br>your body and soul.</p>
      <ul class="pitch__list">
        <li><svg viewBox="0 0 10 10"><circle cx="5" cy="5" r="4.3" fill="none" stroke="#161616" stroke-width=".9"/><path d="M3 5.2l1.4 1.4L7.2 3.6" fill="none" stroke="#161616" stroke-width=".9"/></svg>Restore balance.</li>
        <li><svg viewBox="0 0 10 10"><circle cx="5" cy="5" r="4.3" fill="none" stroke="#161616" stroke-width=".9"/><path d="M3 5.2l1.4 1.4L7.2 3.6" fill="none" stroke="#161616" stroke-width=".9"/></svg>Revive your senses.</li>
      </ul>
    </div>
    <div class="menu">
      <div class="treatment">
        <h3 class="treatment__title">DEEP TISSUE MASSAGE</h3>
        <div class="treatment__rows">
          <div class="option"><div class="option__price">£ 45<span class="option__time">60 min.</span></div><p class="option__desc">Oil massage personalised,<br>light to firm pressure</p></div>
          <div class="option"><div class="option__price">£ 55<span class="option__time">90 min.</span></div><p class="option__desc">Oil massage,<br>medium to firm pressure</p></div>
        </div>
      </div>
      <div class="treatment">
        <h3 class="treatment__title">THAI FLOOR TRADITIONAL MASSAGE</h3>
        <div class="treatment__rows">
          <div class="option"><div class="option__price">£ 45<span class="option__time">60 min.</span></div><p class="option__desc">Dry massage,<br>medium to firm pressure</p></div>
        </div>
      </div>
    </div>
    <p class="opening">OPEN 7 DAYS A WEEK</p>
    <div class="contact">
      <span class="contact__item"><svg viewBox="0 0 10 10"><path d="M2 1l2 2-1 1.3c.6 1.3 1.5 2.2 2.7 2.7L7 6l2 2-1.3 1.3C4.5 9 1 5.5.7 2.3z" fill="#fff"/></svg>01632 960728</span>
      <span class="contact__item"><svg viewBox="0 0 10 10"><path d="M5 .5a3.3 3.3 0 0 0-3.3 3.3C1.7 6.3 5 9.5 5 9.5s3.3-3.2 3.3-5.7A3.3 3.3 0 0 0 5 .5zm0 4.6a1.3 1.3 0 1 1 0-2.6 1.3 1.3 0 0 1 0 2.6z" fill="#fff"/></svg>42 Oak Row, Ashgrove, AG4 2QT</span>
      <span class="contact__item"><svg viewBox="0 0 10 10"><circle cx="5" cy="5" r="4.2" fill="none" stroke="#fff" stroke-width="1"/><ellipse cx="5" cy="5" rx="1.8" ry="4.2" fill="none" stroke="#fff" stroke-width=".8"/><path d="M.8 5h8.4" stroke="#fff" stroke-width=".8"/></svg>www.pelinthaimassage.co.uk</span>
    </div>
  </section>

</div>
</body>
</html>
```